I need two seperate flyers made
I have supplied 2 x photos of bathrooms, one for each flyer.
First flyer i want a banner or some sort of blockout acccross the bottom with my business name Marlow Bathrooms and my number 0487650923 and the promo is '' Renovate your bathroom from $10990 and in small writing under neath say owner to supply fixtures and tiles

Second flyer to have the same banner accross bottom and the promo is
Complete bathroom renovations from $15990 with small writing under saying terms and conditions apply

Want these to look professional and eye cathcing to generate more work.

I have attached 2x of our old flyers for reference and our current logo for use
Looking forward to working with you.

```html
<!DOCTYPE html>
<html lang="en">
<head>
<meta charset="utf-8">
<title>Marlow Bathrooms – Flyers</title>
<link href="https://fonts.googleapis.com/css2?family=Poppins:wght@400;500;600;700;800&display=swap" rel="stylesheet">
<style>
  :root{
    --bg:#d6d6d6;
    --paper:#ffffff;
    --brand-blue:#1a6fc0;
    --ink:#232323;
    --slate:#4a4d52;
    --photo-a:#c9c8c1;
    --photo-b:#9e9c92;
    --photo-c:#c7cdca;
    --photo-d:#8f9794;
  }
  *{box-sizing:border-box;margin:0;padding:0}
  html,body{width:1200px;height:1120px;overflow:hidden;background:var(--bg)}
  body{font-family:"Poppins",sans-serif;position:relative}
  .flyer-slot{position:absolute;top:203px;width:520px;height:713px}
  .flyer-slot--left{left:60px}
  .flyer-slot--right{left:620px}
  .flyer{
    position:absolute;top:0;left:0;width:660px;height:905px;
    transform:scale(0.7879);transform-origin:top left;
    background:linear-gradient(180deg,#fff 0%,#fff 62%,#ececec 90%,#fff 90.1%);
    overflow:hidden;
  }
  .photo-frame{position:absolute;left:48px;top:78px;width:535px;height:474px;background:var(--brand-blue)}
  .photo{position:absolute;left:65px;top:64px;width:532px;height:474px}
  .photo--shower{background:linear-gradient(100deg,var(--photo-a) 0%,#d8d6cf 45%,var(--photo-b) 100%)}
  .photo--vanity{background:linear-gradient(110deg,var(--photo-d) 0%,var(--photo-c) 40%,#dfe2e0 75%,#b9bfbc 100%)}
  .photo-brand{
    position:absolute;left:100px;top:118px;
    color:#fff;font-weight:500;font-size:17px;letter-spacing:3px;
  }
  .headline{
    position:absolute;left:0;width:660px;text-align:center;
    color:var(--ink);font-weight:700;font-size:34px;line-height:35px;
  }
  .price-label{
    position:absolute;left:0;width:660px;text-align:center;
    color:var(--brand-blue);font-weight:600;font-size:13px;
  }
  .price{
    position:absolute;left:0;width:660px;text-align:center;
    color:var(--ink);font-weight:700;font-size:66px;line-height:66px;
  }
  .fine-print{
    position:absolute;left:0;width:660px;text-align:center;
    color:var(--ink);font-weight:400;font-size:11px;
  }
  .banner{position:absolute;left:0;width:660px;height:130px}
  .banner-shape{position:absolute;left:0;top:0}
  .banner-name{
    position:absolute;left:86px;top:36px;
    color:#fff;font-weight:800;font-size:38px;line-height:34px;letter-spacing:0.5px;
  }
  .banner-call{
    position:absolute;right:85px;top:58px;
    color:var(--brand-blue);font-weight:700;font-size:11px;line-height:12px;letter-spacing:0.3px;
    display:flex;align-items:center;gap:4px;
  }
  .banner-call-icon{display:block;flex:none}
  .banner-phone{
    position:absolute;right:85px;top:72px;
    color:var(--ink);font-weight:500;font-size:31px;line-height:36px;letter-spacing:0.5px;
  }
</style>
</head>
<body>

<div class="flyer-slot flyer-slot--left">
  <article class="flyer">
    <div class="photo-frame"></div>
    <div class="photo photo--shower" role="img" aria-label="Photo of a renovated bathroom with floating vanity, oval mirror and gold-fitted walk-in shower"></div>
    <div class="photo-brand">MARLOW BATHROOMS</div>

    <h1 class="headline" style="top:578px">RENOVATE YOUR BATHROOM</h1>
    <p class="price-label" style="top:623px">PRICE STARTS FROM</p>
    <p class="price" style="top:642px">$10 990</p>
    <p class="fine-print" style="top:714px">Owner to supply fixtures and tiles</p>

    <div class="banner" style="top:740px">
      <svg class="banner-shape" width="660" height="130" viewBox="0 0 660 130">
        <polygon points="48,7 330,7 352,25 580,25 580,45 65,45 65,67 48,67" fill="var(--slate)"/>
        <rect x="342" y="43" width="253" height="72" fill="#fff" stroke="var(--brand-blue)" stroke-width="4"/>
        <polygon points="65,25 320,25 395,117 65,117" fill="var(--brand-blue)"/>
      </svg>
      <div class="banner-name">MARLOW<br>BATHROOMS</div>
      <div class="banner-call">
        <svg class="banner-call-icon" width="10" height="10" viewBox="0 0 10 10"><circle cx="5" cy="5" r="5" fill="var(--brand-blue)"/><path d="M3.2 2.6l.9-.3.6 1.3-.5.5c.3.6.7 1 1.3 1.3l.5-.5 1.3.6-.3.9c-2 .1-3.9-1.8-3.8-3.8z" fill="#fff"/></svg>
        <span>CALL US AT</span>
      </div>
      <div class="banner-phone">0487650923</div>
    </div>
  </article>
</div>

<div class="flyer-slot flyer-slot--right">
  <article class="flyer">
    <div class="photo-frame"></div>
    <div class="photo photo--vanity" role="img" aria-label="Photo of a bright bathroom with backlit round mirror, white shaker vanity, freestanding bath and pendant light"></div>
    <div class="photo-brand">MARLOW BATHROOMS</div>

    <h1 class="headline" style="top:564px">COMPLETE<br>BATHROOM RENOVATIONS</h1>
    <p class="price-label" style="top:645px">PRICE STARTS FROM</p>
    <p class="price" style="top:664px">$15 990</p>
    <p class="fine-print" style="top:730px">Terms and conditions apply</p>

    <div class="banner" style="top:752px">
      <svg class="banner-shape" width="660" height="130" viewBox="0 0 660 130">
        <polygon points="48,7 330,7 352,25 580,25 580,45 65,45 65,67 48,67" fill="var(--slate)"/>
        <rect x="342" y="43" width="253" height="72" fill="#fff" stroke="var(--brand-blue)" stroke-width="4"/>
        <polygon points="65,25 320,25 395,117 65,117" fill="var(--brand-blue)"/>
      </svg>
      <div class="banner-name">MARLOW<br>BATHROOMS</div>
      <div class="banner-call">
        <svg class="banner-call-icon" width="10" height="10" viewBox="0 0 10 10"><circle cx="5" cy="5" r="5" fill="var(--brand-blue)"/><path d="M3.2 2.6l.9-.3.6 1.3-.5.5c.3.6.7 1 1.3 1.3l.5-.5 1.3.6-.3.9c-2 .1-3.9-1.8-3.8-3.8z" fill="#fff"/></svg>
        <span>CALL US AT</span>
      </div>
      <div class="banner-phone">0487650923</div>
    </div>
  </article>
</div>

</body>
</html>
```